Stationery Design Project for Pell Co

Hi All,

We need you to design stationary for a new online financial services business. We have already got the logo designed and it is attached. If you would like it in any other formats please let me know. If you could also if possible, match the fonts in your design to that on the logo’s provided.

What we need:
- Business Card
- A4 Letter head
- A4 Folders
- PPT template (Title page and regular page)

And what ever else you want to throw in.

We are in the process of getting the web site designed, however below is a list of websites which we like which will give you an understanding of the style that we are going for.

- vantrela.com
- brimhollow.com
- quellaport.com
- tarnivex.com

I look forward to your seeing your design.

Industry/Entity Type

Financial

Requirements
Must have
• Outputs:
- Documents ready to print
- Generic editable information
- Pdf copies of the documents
- Word version of letterhead

```html
<!DOCTYPE html>
<html lang="en">
<head>
<meta charset="utf-8">
<title>Pell Co Letterhead</title>
<link rel="stylesheet" href="https://fonts.googleapis.com/css2?family=Quicksand:wght@500&family=Arimo:wght@400&display=swap">
<style>
  :root {
    --backdrop: #c4c4c4;
    --paper: #ffffff;
    --brand-blue: #0f7ea8;
    --brand-orange: #f7941d;
    --ink-grey: #4a4a4a;
  }
  html, body {
    margin: 0;
    padding: 0;
    width: 1200px;
    height: 1155px;
    overflow: hidden;
    background: var(--backdrop);
  }
  .letterhead {
    position: absolute;
    left: 195px;
    top: 39px;
    width: 755px;
    height: 1069px;
    background: var(--paper);
  }
  .letterhead__band {
    position: absolute;
    left: 0;
    top: 0;
    width: 100%;
    height: 121px;
    background: var(--brand-blue);
  }
  .brand {
    position: absolute;
    right: 36px;
    top: 22px;
    width: 130px;
    display: flex;
    flex-direction: column;
    align-items: center;
  }
  .brand__dot {
    width: 44px;
    height: 44px;
    border-radius: 50%;
    background: var(--brand-orange);
  }
  .brand__name {
    margin-top: 6px;
    font-family: "Quicksand", sans-serif;
    font-weight: 500;
    font-size: 29px;
    line-height: 1;
    color: var(--paper);
    white-space: nowrap;
  }
  .letterhead__footer {
    position: absolute;
    left: 0;
    right: 0;
    top: 1037px;
    text-align: center;
    font-family: "Arimo", Arial, sans-serif;
    font-size: 14px;
    color: var(--ink-grey);
    white-space: nowrap;
  }
</style>
</head>
<body>
  <main class="letterhead">
    <header class="letterhead__band">
      <div class="brand">
        <span class="brand__dot"></span>
        <span class="brand__name">Pell Co</span>
      </div>
    </header>
    <footer class="letterhead__footer">
      City, State Name, 31 StreetName str &bull; Phone: 555-014-7720 &bull; Fax: 555-014-7720 &bull; www.pellcofinance.com
    </footer>
  </main>
</body>
</html>
```